Redesign www.KORVADA.ch - Shopwell Web-Shop - Storytelling

Redesign of existing Shopwell Web-page of KOR-VADA.ch.
Please carefully review both enclosed documents. The annotated notes explain the expected design direction and priorities.

```html
<!DOCTYPE html>
<html lang="en">
<head>
<meta charset="utf-8">
<title>KOR-VADA – Handmade Scarves</title>
<link href="https://fonts.googleapis.com/css2?family=Cormorant+Garamond:wght@400;500&family=Crimson+Pro:wght@400;600&display=swap" rel="stylesheet">
<style>
:root{
  --ink:#2f2f33;
  --muted:#5c5c62;
  --accent:#4c5874;
  --line:#d9d9de;
  --product-bg:#f1eff0;
  --white:#ffffff;
}
*{box-sizing:border-box;margin:0;padding:0}
html,body{width:1200px;height:4768px;overflow:hidden;background:var(--white)}
body{position:relative;font-family:"Crimson Pro",Georgia,serif;color:var(--ink)}
.abs{position:absolute}
.serif-display{font-family:"Cormorant Garamond",Georgia,serif;font-weight:400;color:var(--ink)}
.btn{position:absolute;background:var(--accent);color:var(--white);font-size:16px;letter-spacing:.3px;display:flex;align-items:center;justify-content:center;text-transform:uppercase;font-weight:600}
.announcement{top:0;left:0;width:1200px;height:45px;border-bottom:1px solid var(--line);display:flex;align-items:center;justify-content:center;font-size:16px}
.header{top:45px;left:0;width:1200px;height:100px;border-bottom:1px solid var(--line)}
.logo{left:111px;top:14px;width:70px;height:70px;background:#4a4a4e;color:var(--white);display:flex;flex-direction:column;align-items:center;justify-content:center;font-weight:600;font-size:13px;line-height:1.1}
.logo small{font-size:7px;font-weight:600}
.nav a{position:absolute;top:40px;font-size:17px;color:var(--ink);text-decoration:none;letter-spacing:.5px}
.nav .current{text-decoration:underline;text-underline-offset:4px}
.hero{top:145px;left:0;width:1200px;height:500px;background:linear-gradient(90deg,#e6e9ee 0%,#d6dce4 45%,#9aa4b2 62%,#3f4658 78%,#b9a999 100%)}
.hero h1{position:absolute;left:111px;top:86px;width:460px;font-size:46px;line-height:46px}
.hero p{position:absolute;left:111px;top:244px;width:440px;font-size:23px;line-height:30px}
.features .item{position:absolute;top:713px;width:240px;text-align:center;font-size:22px;line-height:28px}
.features svg{display:block;margin:0 auto 25px}
.story-photo{left:111px;top:924px;width:489px;height:446px;background:linear-gradient(135deg,#9aa0a8,#d8a640 45%,#6f6a6a)}
.story h2{position:absolute;left:656px;top:980px;font-size:44px;line-height:46px}
.story p{position:absolute;left:656px;top:1092px;width:434px;font-size:20px;line-height:27px}
.section-title{position:absolute;left:0;width:1200px;text-align:center;font-size:42px}
.card{position:absolute;width:224px}
.card .photo{height:258px;background:var(--product-bg);position:relative}
.card .name{margin-top:20px;font-size:17.5px;line-height:25px;width:234px}
.card .price{margin-top:6px;font-size:17px;color:var(--accent);font-weight:600}
.sold{position:absolute;left:10px;bottom:10px;padding:0 18px;height:30px;border-radius:15px;background:#3f3f43;color:var(--white);font-size:14px;font-weight:600;display:flex;align-items:center}
.caption{position:absolute;font-size:17px;line-height:28px;text-transform:uppercase;letter-spacing:.3px}
.quote{position:absolute;top:3476px;width:260px;text-align:center}
.quote h3{margin:24px auto 0;width:220px;font-size:18px;line-height:22px;font-weight:600}
.quote p{margin-top:8px;font-size:16px;line-height:21px;color:var(--muted)}
.newsletter{top:3765px;left:0;width:1200px;height:428px;background:linear-gradient(90deg,#dfe6ee 0%,#e9eef3 50%,#cfd8e1 70%,#e8b5a9 82%,#dfe6ee 100%)}
.newsletter h2{position:absolute;left:111px;top:94px;font-size:46px}
.newsletter p{position:absolute;left:111px;top:176px;width:545px;font-size:23px;line-height:30px}
.footer h4{position:absolute;top:4288px;font-size:18px;font-weight:600}
.footer ul{position:absolute;top:4326px;list-style:none;font-size:16px;line-height:24px;color:var(--muted)}
.footer li::before{content:"•";color:var(--ink);margin-right:18px}
.mission{left:611px;top:4326px;width:480px;font-size:16px;line-height:24px;color:var(--muted)}
.field{position:absolute;border:1px solid #9a9aa0;display:flex;align-items:center;justify-content:space-between;padding:0 16px;font-size:16px;color:var(--muted)}
.social{position:absolute;top:4503px;width:16px;height:16px;border:2px solid var(--ink);border-radius:50%}
.divider{position:absolute;left:111px;top:4584px;width:978px;height:1px;background:var(--line)}
.payments{position:absolute;left:846px;top:4668px;display:flex;gap:8px}
.payments span{font-size:12px;color:var(--accent);font-weight:600;border:1px solid var(--line);padding:2px 5px;border-radius:3px}
.copyright{position:absolute;left:111px;top:4722px;font-size:13px}
</style>
</head>
<body>

<div class="abs announcement">Unique items - made with love by Mirela - Handmade</div>

<header class="abs header">
  <div class="abs logo">KOR-VADA<small>Swiss Handmade</small></div>
  <nav class="nav">
    <a class="current" style="left:239px">HOME</a>
    <a style="left:324px">COLLECTION</a>
    <a style="left:472px">PRODUCT</a>
  </nav>
  <svg class="abs" style="left:970px;top:40px" width="120" height="20" viewBox="0 0 120 20" fill="none" stroke="#2f2f33" stroke-width="2">
    <circle cx="8" cy="8" r="5.5"/><line x1="12" y1="12" x2="17" y2="17"/>
    <circle cx="58" cy="6" r="4" fill="#2f2f33"/><path d="M51 17c0-5 14-5 14 0z" fill="#2f2f33"/>
    <path d="M99 7h18l-2 10h-14z M103 7l3-5 M113 7l-3-5"/>
  </svg>
</header>

<section class="abs hero" role="img" aria-label="Woman wearing a colourful patterned scarf by the sea">
  <h1 class="serif-display">Handmade Unique<br>Pieces for Women with<br>Style.</h1>
  <p>Each KOR-VADA scarf is one of a kind – carefully crafted to add personality to your outfit.</p>
  <div class="btn" style="left:111px;top:357px;width:202px;height:46px">Discover scarves</div>
</section>

<section class="features">
  <div class="item" style="left:91px">
    <svg width="58" height="58" viewBox="0 0 58 58" fill="none" stroke="#4c5874" stroke-width="2"><path d="M6 16h46M6 29h46M6 42h46M16 6v46M29 6v46M42 6v46"/><rect x="6" y="6" width="46" height="46" rx="6"/></svg>
    Handmade locally in<br>Switzerland</div>
  <div class="item" style="left:334px">
    <svg width="58" height="58" viewBox="0 0 58 58" fill="none" stroke="#4c5874" stroke-width="2"><path d="M16 4h26v8H16zM20 12v34M38 12v34M20 46l-2 8M25 46v8M33 46v8M38 46l2 8M20 46h18"/></svg>
    Only 1–3 pieces per<br>design</div>
  <div class="item" style="left:578px">
    <svg width="58" height="58" viewBox="0 0 58 58" fill="none" stroke="#4c5874" stroke-width="2"><circle cx="29" cy="36" r="16"/><circle cx="29" cy="36" r="9"/><path d="M14 8l2 4 4 .5-3 3 .8 4-3.8-2-3.8 2 .8-4-3-3 4-.5zM29 3l2 4 4 .5-3 3 .8 4-3.8-2-3.8 2 .8-4-3-3 4-.5zM44 8l2 4 4 .5-3 3 .8 4-3.8-2-3.8 2 .8-4-3-3 4-.5z"/></svg>
    High-quality fabrics<br>without scratching</div>
  <div class="item" style="left:850px">
    <svg width="58" height="58" viewBox="0 0 58 58" fill="none" stroke="#4c5874" stroke-width="2"><path d="M8 40c8-2 14 2 22 2s14-4 20-10M8 48c10 0 20 2 30-4M22 30c6-14 18-22 30-24-4 12-14 22-30 24z"/></svg>
    Lightweight and suitable<br>for everyday use</div>
</section>

<section class="story">
  <div class="abs story-photo" role="img" aria-label="Hands knitting mustard yellow yarn on wooden needles"></div>
  <h2 class="serif-display">A Story Woven<br>Through Generations</h2>
  <p>Fabrics have been part of my life since childhood. My grandmother and my mother created with their hands – and this is exactly what I continue today. I consciously take my time for each piece...</p>
  <div class="btn" style="left:656px;top:1256px;width:198px;height:48px">View new pieces</div>
</section>

<h2 class="section-title serif-display" style="top:1462px">Latest Products</h2>

<section class="products">
  <div class="card" style="left:111px;top:1552px"><div class="photo" role="img" aria-label="Beige knit top on mannequin with mint and pink scarf"></div><div class="name">Elvina triangular scarf/small scarf, beige, mint, pink</div><div class="price">CHF 39.00</div></div>
  <div class="card" style="left:362px;top:1552px"><div class="photo" role="img" aria-label="Mannequin with vanilla, red and olive small scarf"></div><div class="name">Marelle triangular scarf/small scarf, vanilla, red, olive green</div><div class="price">CHF 39.00</div></div>
  <div class="card" style="left:613px;top:1552px"><div class="photo" role="img" aria-label="Mannequin with spring coloured scarf"></div><div class="name">Odessa women's triangular scarf, women's scarf, spring colors</div><div class="price">CHF 39.00</div></div>
  <div class="card" style="left:864px;top:1552px"><div class="photo" role="img" aria-label="Mannequin with pink and turquoise small scarf"></div><div class="name">Verena triangular scarf/small scarf, pink, vanilla, turquoise, green</div><div class="price">CHF 39.00</div></div>

  <div class="card" style="left:111px;top:1967px"><div class="photo" role="img" aria-label="Denim jacket on mannequin with rust linen scarf"></div><div class="name">Women's triangular scarf Liliane, women's scarf, linen scarf</div><div class="price">CHF 69.00</div></div>
  <div class="card" style="left:362px;top:1967px"><div class="photo" role="img" aria-label="Denim jacket on mannequin with beige linen scarf"><span class="sold">Sold Out</span></div><div class="name">Corinna women's triangular scarf, women's scarf, linen scarf, beige</div><div class="price">CHF 69.00</div></div>
  <div class="card" style="left:613px;top:1967px"><div class="photo" role="img" aria-label="Denim jacket on mannequin with pale pink linen scarf"></div><div class="name">Women's triangular scarf Nella, women's scarf, linen scarf, pale pink</div><div class="price">CHF 69.00</div></div>
  <div class="card" style="left:864px;top:1967px"><div class="photo" role="img" aria-label="Denim jacket on mannequin with olive and anthracite scarf"></div><div class="name">Talia women's triangular scarf, women's scarf, light olive, anthracite</div><div class="price">CHF 69.00</div></div>
</section>

<h2 class="abs serif-display" style="left:111px;top:2414px;font-size:40px">Everyday Use &amp; Uniqueness</h2>
<section class="everyday">
  <div class="abs" style="left:111px;top:2498px;width:600px;height:719px;background:linear-gradient(160deg,#e9e7e3,#cfc9c2 55%,#8d8a88)" role="img" aria-label="Smiling woman in knit hat and chunky grey scarf"></div>
  <div class="caption" style="left:111px;top:3234px">From fabric to finished piece</div>
  <div class="card" style="left:745px;top:2498px;width:344px"><div class="photo" style="height:299px" role="img" aria-label="White blouse on mannequin with orange and black scarf"></div><div class="name" style="width:290px;margin-top:20px">Senna women's triangular scarf, women's scarf</div><div class="price">CHF 69.00</div></div>
  <div class="abs" style="left:745px;top:2919px;width:344px;height:298px;background:linear-gradient(135deg,#b08a8c,#d7cbc1 45%,#7fb2cf 60%,#c89a9c)" role="img" aria-label="Woman in floral dress carrying a light blue handbag"></div>
  <div class="caption" style="left:745px;top:3234px">Designed for everyday<br>moments</div>
</section>

<h2 class="section-title serif-display" style="top:3366px">What Our Customers Say</h2>
<section class="reviews">
  <div class="quote" style="left:135px"><svg width="40" height="32" viewBox="0 0 40 32" fill="#4c5874"><path d="M0 32V16C0 6 6 1 16 0v6c-5 1-8 4-8 9h8v17zM22 32V16c0-10 6-15 16-16v6c-5 1-8 4-8 9h8v17z"/></svg><h3>My favorite scarf – I already own several.</h3><p>Lorem ipsum dolor sit amet, consectetur adipiscing elit, sed do eiusmod tempor incididunt ut labore et dolore magna aliqua. Ut enim ad minim veniamea.</p></div>
  <div class="quote" style="left:468px"><svg width="40" height="32" viewBox="0 0 40 32" fill="#4c5874"><path d="M0 32V16C0 6 6 1 16 0v6c-5 1-8 4-8 9h8v17zM22 32V16c0-10 6-15 16-16v6c-5 1-8 4-8 9h8v17z"/></svg><h3>My favorite scarf – I already own several.</h3><p>Lorem ipsum dolor sit amet, consectetur adipiscing elit, sed do eiusmod tempor incididunt ut labore et dolore magna aliqua. Ut enim ad minim veniamea.</p></div>
  <div class="quote" style="left:803px"><svg width="40" height="32" viewBox="0 0 40 32" fill="#4c5874"><path d="M0 32V16C0 6 6 1 16 0v6c-5 1-8 4-8 9h8v17zM22 32V16c0-10 6-15 16-16v6c-5 1-8 4-8 9h8v17z"/></svg><h3>My favorite scarf – I already own several.</h3><p>Lorem ipsum dolor sit amet, consectetur adipiscing elit, sed do eiusmod tempor incididunt ut labore et dolore magna aliqua. Ut enim ad minim veniamea.</p></div>
</section>

<section class="abs newsletter" role="img" aria-label="Woman with sunglasses and colourful headscarf">
  <h2 class="serif-display">Stay Connected</h2>
  <p>Find out when new models are released and where you can meet KOR-VADA in person. I also share tips on how to wear the scarves.</p>
  <div class="btn" style="left:111px;top:280px;width:254px;height:44px">Discover scarves now</div>
</section>

<footer class="footer">
  <h4 style="left:111px">Quick links</h4>
  <ul style="left:111px"><li>Home</li><li>Collection</li><li>Product</li></ul>
  <h4 style="left:291px">Info</h4>
  <ul style="left:291px"><li>Shipping information</li><li>Terms &amp; Conditions</li><li>Imprint</li></ul>
  <h4 style="left:611px">Our mission</h4>
  <p class="abs mission">You will be among the first to be informed about new collections and exclusive offers.</p>

  <h4 style="top:4446px;left:111px">Subscribe to our emails</h4>
  <div class="field" style="left:111px;top:4489px;width:487px;height:43px">Email
    <svg width="22" height="14" viewBox="0 0 22 14" fill="none" stroke="#2f2f33" stroke-width="1.6"><path d="M0 7h20M14 1l6 6-6 6"/></svg></div>
  <span class="social" style="left:1035px"></span>
  <span class="social" style="left:1072px"></span>

  <div class="divider"></div>
  <h4 style="top:4614px;left:111px">Country/region</h4>
  <div class="field" style="left:111px;top:4656px;width:256px;height:42px">Switzerland | CHF
    <svg width="10" height="6" viewBox="0 0 10 6" fill="none" stroke="#2f2f33" stroke-width="1.4"><path d="M1 1l4 4 4-4"/></svg></div>
  <div class="payments"><span>Amvio</span><span>Pomo Pay</span><span>Cirka</span><span>Lianpay</span><span>Vexa</span></div>
  <div class="copyright">© 2026, KOR-VADA Powered by Shopwell</div>
</footer>

</body>
</html>
```